Web Design Project (Renewable Energy Services Company)

Hello crowd,

We are looking to create a website for a new company. We would like to have the page already coded, if you do not provide the code as well, please indicate so. I am including a very preliminary approximation of the wireframe.

We do not have the logo either the color pallet, however we have in mind couple websites that would be similar tho these.

http://www.brivolen.com/en/

and

http://www.tarmuvex.com/

We did an approximated wireframe our our website, not necesarly to decide on the layout but rather to know how many pages will be needed. It would be around 10 pages. We will need a section that will be an e-commerce page to sell products such as engineering instrumentation, software and consumables such as cable and connectors.

Our company will be called ORVIK. We will be based in Monterrey, Mexico. Our focused will be the development of renewable energy projects. Similar scope of services than http://www.brivolen.com/en/ but only for wind and solar projects.

We like something minimalistic. Some of the things that the logo might or might not include would be the monterrey famous hill, but not strictly necessary.
http://en.plavorinet.org/wiki/Loma_del_Trueno

also ORVIK (which stands for ORganica VIKtoria) the name is similar the bird (seagal) or wind turbines and sun...any of these are only suggestions and we are open to receive any proposals.

There must be a
home page
services page (some subsections)
products page (some subsections)
contact page with contact form

and some additional subsections like careers and partnerships.

We are very excited to start hearing about this project.
Updates

Please for the logo, do not restrict your ideas to the ones provided as it has generated too specific logos. Pleae just allow your imagination to flow for a company that develops renewable energy projects.

Target Market(s)

large companies interested in developing renewable energy projects

Industry/Entity Type

E-Commerce

Requirements
Must have
• Minimalistic and unique design.
Nice to have
• contact form to save contacts in a database

Should not have
• We are looking a very minimalistic logo. It should not be an explicit wind turbine a seagal or anything like that. we are looking for abstract, simple and minimalistic image.

```html
<!DOCTYPE html>
<html lang="es">
<head>
<meta charset="utf-8">
<title>Orvik — Proyectos Renovables</title>
<link rel="stylesheet" href="https://fonts.googleapis.com/css2?family=Source+Sans+3:wght@400;500;600;700&family=Arimo:wght@400;700&display=swap">
<style>
  :root{
    --nav-bg:#232323;
    --page-bg:#ececec;
    --green:#6ea324;
    --green-light:#8cc63e;
    --green-dark:#4f8a12;
    --ink:#1b1b1b;
    --muted:#7a7a7a;
    --white:#ffffff;
    --frame:#ffffff;
    --footer-top:#8ccb2c;
    --footer-bottom:#5d9a12;
  }
  *{box-sizing:border-box;margin:0;padding:0}
  html,body{width:1200px;height:1104px;overflow:hidden}
  body{
    position:relative;
    background:var(--page-bg);
    font-family:"Source Sans 3",sans-serif;
    color:var(--ink);
  }
  .abs{position:absolute}

  /* top navigation */
  .topbar{left:0;top:0;width:1200px;height:44px;background:var(--nav-bg)}
  .nav-item{top:0;height:44px;line-height:40px;color:var(--white);font-size:16px;font-weight:600;text-decoration:none}
  .nav-item.is-active{
    top:4px;height:30px;line-height:28px;padding:0 19px;
    background:linear-gradient(var(--green-light),var(--green-dark));
    border:1px solid #cfe9a8;
  }
  .search{left:920px;top:10px;width:160px;height:27px;background:var(--white);padding-left:16px;font-size:13px;line-height:27px;color:#222}
  .search-btn{left:1073px;top:7px}

  /* brand row */
  .brand{left:118px;top:68px;display:flex;align-items:center;gap:18px}
  .brand-dot{width:88px;height:88px;border-radius:50%;background:var(--green)}
  .brand-name{font-size:64px;font-weight:700;color:var(--green);letter-spacing:1px}
  .cart-line{left:760px;top:93px;font-size:14px;color:var(--ink)}
  .cart-line a{color:var(--green);text-decoration:none}
  .cart-icon{left:1054px;top:84px}

  /* hero */
  .hero-halo{
    left:102px;top:186px;width:446px;height:435px;border-radius:50%;
    background:radial-gradient(circle at 50% 50%,rgba(140,198,62,.55) 0%,rgba(190,225,150,.45) 55%,rgba(236,236,236,0) 72%);
  }
  .hero-globe{
    left:200px;top:296px;width:250px;height:250px;border-radius:50%;
    background:radial-gradient(circle at 38% 34%,#d9f1b6 0%,#8fd05a 28%,#3fa238 62%,#1e7a2a 100%);
    box-shadow:0 0 0 8px #e6f3d6,0 0 0 11px #5daa33;
  }
  .hero-title{left:609px;top:216px;font-size:31px;font-weight:700;color:var(--green);letter-spacing:.3px}
  .hero-sub{left:609px;top:254px;font-size:31px;font-weight:400;color:var(--ink);letter-spacing:.6px}
  .service-list{left:616px;top:335px;list-style:none;font-size:14.5px;line-height:20.8px;font-weight:500;color:var(--ink)}
  .hero-icon{
    left:932px;top:353px;width:125px;height:146px;border-radius:50% 50% 12px 12px;
    background:radial-gradient(circle at 40% 25%,#fbf1a4 0%,#f2e37a 20%,#8ad45c 50%,#2f9a3a 100%);
  }

  /* product cards */
  .card{top:664px;width:232px}
  .card-title{font-size:17.5px;font-weight:400;color:#333;height:36px;padding-left:4px}
  .card-frame{width:229px;height:161px;background:var(--frame);padding:5px;box-shadow:0 0 0 1px #dcdcdc;position:relative}
  .card-photo{width:100%;height:100%}
  .card-badge{position:absolute;right:8px;bottom:-5px}
  .card-text{margin-top:21px;padding-left:8px;font-family:"Arimo",sans-serif;font-size:13px;line-height:18.8px;letter-spacing:.2px;color:var(--muted);width:222px}
  .card-text b{color:var(--green)}

  /* footer */
  .footer{left:0;top:1015px;width:1200px;height:89px;background:linear-gradient(var(--footer-top),var(--footer-bottom))}
  .footer-mark{left:102px;top:1029px;width:68px;height:64px;border-radius:50%;background:radial-gradient(circle at 45% 40%,#b6e07a,#3f7f12)}
  .footer-links{left:195px;top:1032px;font-size:15.5px;color:var(--white)}
  .footer-links a{color:var(--white)}
  .footer-links .sep{margin:0 16px;color:#333}
  .footer-links .dim{color:#2e3a1e;text-decoration:none}
  .footer-sub{left:196px;top:1075px;font-family:"Arimo",sans-serif;font-size:12px;color:var(--white)}
  .footer-sub .sep{margin:0 12px}
  .copyright{left:543px;top:1074px;font-size:15px;font-weight:600;color:var(--white)}
  .mail-icon{left:802px;top:1039px}
  .contact-title{left:882px;top:1019px;font-size:20px;color:var(--white);font-weight:500}
  .contact-address{left:881px;top:1054px;font-size:13px;line-height:25px;color:var(--white);font-weight:600;font-style:normal}
</style>
</head>
<body>

<header>
  <div class="abs topbar"></div>
  <nav>
    <a class="abs nav-item is-active" style="left:104px" href="#">Inicio</a>
    <a class="abs nav-item" style="left:227px" href="#">Servicios</a>
    <a class="abs nav-item" style="left:345px" href="#">Productos</a>
    <a class="abs nav-item" style="left:471px" href="#">Nuestra</a>
    <a class="abs nav-item" style="left:585px" href="#">Especialidad</a>
    <a class="abs nav-item" style="left:732px" href="#">Contacto</a>
  </nav>
  <div class="abs search">Search here</div>
  <svg class="abs search-btn" width="34" height="34" viewBox="0 0 34 34" aria-hidden="true">
    <defs><radialGradient id="btnGrad" cx="40%" cy="35%"><stop offset="0" stop-color="#b7e36a"/><stop offset="1" stop-color="#4f8a12"/></radialGradient></defs>
    <circle cx="17" cy="17" r="16" fill="url(#btnGrad)"/>
    <circle cx="15" cy="15" r="6" fill="none" stroke="#fff" stroke-width="2.5"/>
    <line x1="19.5" y1="19.5" x2="25" y2="25" stroke="#fff" stroke-width="3" stroke-linecap="round"/>
  </svg>

  <div class="abs brand">
    <span class="brand-dot"></span>
    <span class="brand-name">ORVIK</span>
  </div>
  <p class="abs cart-line">You have no item in your Cart <a href="#">Checkout &gt;&gt;</a></p>
  <svg class="abs cart-icon" width="36" height="32" viewBox="0 0 36 32" aria-hidden="true">
    <path d="M2 4h6l4 17h18l4-12H10" fill="none" stroke="#8cc63e" stroke-width="2.5" stroke-linejoin="round"/>
    <circle cx="14" cy="27" r="2.6" fill="#8cc63e"/><circle cx="28" cy="27" r="2.6" fill="#8cc63e"/>
  </svg>
</header>

<main>
  <div class="abs hero-halo" role="img" aria-label="Ilustración de un globo terráqueo verde rodeado de aerogeneradores, árboles, paneles solares y una figura de negocios"></div>
  <div class="abs hero-globe" aria-hidden="true"></div>
  <h1 class="abs hero-title">Proyectos Renovables</h1>
  <h2 class="abs hero-sub">Para México y Latino América</h2>
  <ul class="abs service-list">
    <li>Energía Eólica</li>
    <li>Proyectos de Generación Eólica desde 1MW</li>
    <li>hasta 200MW</li>
    <li>Análisis Detallado de Recurso Eólico</li>
    <li>Diseño de Parques Eólicos</li>
    <li>Permitología</li>
    <li>Comisión Nacional de Redes Eléctricas CNRE</li>
    <li>SEDAVEN</li>
    <li>CRV</li>
    <li>Análisis de Riesgo y Factibilidad Financiera</li>
    <li>PPA and Tariff Analysis</li>
  </ul>
  <div class="abs hero-icon" role="img" aria-label="Ilustración de una casa verde con un aerogenerador y un sol detrás"></div>

  <section>
    <article class="abs card" style="left:111px">
      <h3 class="card-title">Contrary to popular belief</h3>
      <div class="card-frame">
        <div class="card-photo" role="img" aria-label="Fotografía de espejos de una planta termosolar bajo cielo azul" style="background:linear-gradient(170deg,#4f86c8 0%,#a9c2dc 30%,#c9d6e2 48%,#a89a86 66%,#8a6e54 100%)"></div>
        <svg class="card-badge" width="30" height="36" viewBox="0 0 30 36" aria-hidden="true"><path d="M15 0L30 10V36H0V10Z" fill="#8cc63e"/><path d="M7 17h3l2 8h9l2-6H11" fill="none" stroke="#fff" stroke-width="1.6"/></svg>
      </div>
      <p class="card-text">Contrary to popular belief lorem Ipsum is not simply random text. Lorem Ipsum is simply dummy text of the typesetting industry.<b>[+]</b></p>
    </article>

    <article class="abs card" style="left:362px">
      <h3 class="card-title">The point of using Lorem</h3>
      <div class="card-frame">
        <div class="card-photo" role="img" aria-label="Fotografía de aerogeneradores sobre colinas verdes bajo cielo nublado" style="background:linear-gradient(#eceeef 0%,#d4d8da 42%,#8bb05a 55%,#5f8e2e 75%,#41701f 100%)"></div>
        <svg class="card-badge" width="30" height="36" viewBox="0 0 30 36" aria-hidden="true"><path d="M15 0L30 10V36H0V10Z" fill="#8cc63e"/><path d="M7 17h3l2 8h9l2-6H11" fill="none" stroke="#fff" stroke-width="1.6"/></svg>
      </div>
      <p class="card-text">Contrary to popular belief lorem Ipsum is not simply random text. Lorem Ipsum is simply dummy text of the typesetting industry.<b>[+]</b></p>
    </article>

    <article class="abs card" style="left:612px">
      <h3 class="card-title">The standard chunk</h3>
      <div class="card-frame">
        <div class="card-photo" role="img" aria-label="Fotografía de paneles solares en un campo de flores con nubes blancas" style="background:linear-gradient(#4a86d0 0%,#dfe8f4 26%,#f4f6f9 38%,#5a82c0 52%,#27508f 70%,#c9c43e 86%,#6e9a2c 100%)"></div>
        <svg class="card-badge" width="30" height="36" viewBox="0 0 30 36" aria-hidden="true"><path d="M15 0L30 10V36H0V10Z" fill="#8cc63e"/><path d="M7 17h3l2 8h9l2-6H11" fill="none" stroke="#fff" stroke-width="1.6"/></svg>
      </div>
      <p class="card-text">Contrary to popular belief lorem Ipsum is not simply random text. Lorem Ipsum is simply dummy text of the typesetting industry.<b>[+]</b></p>
    </article>

    <article class="abs card" style="left:860px">
      <h3 class="card-title">All the Lorem Ipsum</h3>
      <div class="card-frame">
        <div class="card-photo" role="img" aria-label="Fotografía de un parque eólico sobre un campo verde bajo cielo azul" style="background:linear-gradient(#1b73bf 0%,#6fb3e2 35%,#c6e2ef 52%,#8fae4a 58%,#5f8a2a 75%,#3b6418 100%)"></div>
        <svg class="card-badge" width="30" height="36" viewBox="0 0 30 36" aria-hidden="true"><path d="M15 0L30 10V36H0V10Z" fill="#8cc63e"/><path d="M7 17h3l2 8h9l2-6H11" fill="none" stroke="#fff" stroke-width="1.6"/></svg>
      </div>
      <p class="card-text">Contrary to popular belief lorem Ipsum is not simply random text. Lorem Ipsum is simply dummy text of the typesetting industry.<b>[+]</b></p>
    </article>
  </section>
</main>

<footer>
  <div class="abs footer"></div>
  <div class="abs footer-mark" role="img" aria-label="Símbolo de reciclaje verde alrededor de un globo"></div>
  <p class="abs footer-links"><a href="#">Energía Eólica</a><span class="sep">|</span><a class="dim" href="#">Energía Solar</a></p>
  <p class="abs footer-sub">Carreras<span class="sep">|</span>Quienes Somos</p>
  <p class="abs copyright">ORVIK S.A. de C.V. ©</p>
  <svg class="abs mail-icon" width="64" height="60" viewBox="0 0 64 60" aria-hidden="true">
    <g transform="rotate(-12 32 30)">
      <rect x="6" y="12" width="52" height="38" rx="2" fill="#f4f4f4" stroke="#cfcfcf"/>
      <path d="M6 14l26 20 26-20" fill="none" stroke="#bdbdbd" stroke-width="1.5"/>
      <rect x="16" y="4" width="28" height="20" fill="#fff" stroke="#ddd"/>
      <rect x="20" y="8" width="8" height="7" fill="#f39a1e"/>
    </g>
  </svg>
  <h4 class="abs contact-title">Contact Us</h4>
  <address class="abs contact-address">Almendros 218, Col. Jardines del<br>Valle, Monterrey, N.L. 64730</address>
</footer>

</body>
</html>
```